Elegant One-Page Flyer That Catches People's Eye

For a series of workshops and zoom calls I am marketing with a colleague of mine, we would like to have an elegant, catchy one-page flyer that entices people to contact us. I am envisioning a one-page flyer (a card that is somewhat larger than a postcard) with great text, layout and images which magnetically draws people to us and is positive and inspiring. Also, if at all possible, a QR code linking it to our websites. Good colours would be shades of blue and green. I am uploading: the Text, our pictures, logos and contact information.

```html
<!DOCTYPE html>
<html lang="en">
<head>
<meta charset="utf-8">
<title>Lumenpath – Rising Above Hidden Career Deal Breakers</title>
<link rel="stylesheet" href="https://fonts.googleapis.com/css2?family=Open+Sans:wdth,wght@75..100,300..800&display=swap">
<style>
  :root {
    --page-bg: #c9c9c9;
    --green: #2f6a1f;
    --green-soft: #4d7f3a;
    --sky-top: #f7efb4;
    --sky-mid: #f1dc98;
    --dusk: #e3a36f;
    --dusk-deep: #c9835c;
    --band: #efebe8;
    --text-dark: #3f3a2e;
  }
  * { box-sizing: border-box; margin: 0; padding: 0; }
  html, body { width: 1200px; height: 900px; overflow: hidden; }
  body {
    background: var(--page-bg);
    font-family: "Open Sans", Arial, sans-serif;
    display: flex; align-items: center; justify-content: center;
  }
  .flyer {
    position: relative;
    width: 1100px; height: 760px;
    overflow: hidden;
    background: var(--sky-top);
  }
  .flyer__landscape {
    position: absolute; inset: 0;
    background:
      radial-gradient(circle at 78% 18%, #fffbe6 0, rgba(255,251,230,.85) 40px, rgba(255,246,200,0) 160px),
      linear-gradient(180deg, var(--sky-top) 0%, var(--sky-mid) 38%, var(--dusk) 70%, var(--dusk-deep) 100%);
  }
  .portrait {
    position: absolute;
  }
  .portrait--left {
    left: 0; top: 40px; width: 320px; height: 590px;
    background: linear-gradient(180deg, rgba(80,70,60,.0) 0%, #8a6f60 25%, #c9a08a 45%, #3a302c 75%, #1d1a19 100%);
    -webkit-mask-image: linear-gradient(90deg, #000 70%, transparent 100%);
            mask-image: linear-gradient(90deg, #000 70%, transparent 100%);
  }
  .portrait--right {
    right: 20px; top: 160px; width: 290px; height: 520px;
    background: linear-gradient(180deg, #6a4a3a 0%, #d2a48c 25%, #8a6a9a 50%, #76598c 100%);
    border-radius: 140px 140px 0 0;
  }
  .bottom-band {
    position: absolute; left: 0; right: 0; bottom: 0; height: 140px;
    background: linear-gradient(180deg, rgba(239,235,232,.85) 0%, var(--band) 30%);
  }
  .content {
    position: absolute; left: 300px; right: 280px; top: 0;
    text-align: center; color: var(--green);
  }
  .brand {
    margin-top: 58px;
    display: flex; align-items: center; justify-content: center; gap: 14px;
  }
  .brand__dot {
    width: 46px; height: 46px; border-radius: 50%;
    border: 2px solid var(--green-soft);
  }
  .brand__name {
    font-size: 40px; font-weight: 400; letter-spacing: 1px; color: var(--green-soft);
  }
  .headline {
    margin-top: 26px;
    font-size: 29px; font-weight: 800; font-stretch: 88%;
    color: var(--green); letter-spacing: .2px;
  }
  .subhead {
    margin-top: 4px;
    font-size: 19px; font-weight: 400; font-stretch: 75%;
    color: var(--text-dark);
  }
  .programme-title {
    margin-top: 26px;
    font-size: 15px; font-weight: 800; letter-spacing: .6px;
  }
  .format-label {
    margin-top: 16px;
    font-size: 15px; font-weight: 800;
  }
  .format-text {
    font-size: 16px; font-weight: 300; line-height: 1.15; color: var(--green);
  }
  .breakers {
    margin: 24px 14px 0;
    padding: 16px 22px 18px;
    border: 1.5px solid var(--green);
    border-radius: 22px;
    background: rgba(255,246,200,.18);
  }
  .breakers__title {
    font-size: 15px; font-weight: 800; line-height: 1.15;
  }
  .breakers__list {
    margin-top: 8px;
    text-align: left; list-style: none;
    font-size: 16px; font-weight: 400; color: var(--green); line-height: 1.4;
  }
  .breakers__list li { display: flex; gap: 4px; }
  .person {
    position: absolute; color: var(--green); text-align: center;
  }
  .person--left { left: 40px; bottom: 52px; width: 260px; }
  .person--right { right: 28px; bottom: 14px; width: 260px; }
  .person__name { font-size: 15px; font-weight: 800; font-stretch: 88%; }
  .person__bio { font-size: 10px; font-weight: 600; font-stretch: 75%; line-height: 1.3; }
  .contact {
    position: absolute; left: 360px; width: 420px; bottom: 18px;
    text-align: center; color: var(--green);
  }
  .contact__title { font-size: 15px; font-weight: 800; font-stretch: 88%; line-height: 1.15; }
  .contact__line { font-size: 15px; font-weight: 400; font-stretch: 75%; color: var(--green); line-height: 1.3; }
</style>
</head>
<body>
  <main class="flyer">
    <div class="flyer__landscape" role="img" aria-label="Warm sunset over a hazy mountain landscape"></div>
    <div class="portrait portrait--left" role="img" aria-label="Portrait photo of Dr. Helena Marwick, smiling, wearing glasses"></div>
    <div class="portrait portrait--right" role="img" aria-label="Portrait photo of Dr. Clara Venner in a purple cardigan, arms crossed"></div>
    <div class="bottom-band"></div>

    <section class="content">
      <div class="brand">
        <span class="brand__dot"></span>
        <span class="brand__name">LUMENPATH</span>
      </div>
      <h1 class="headline">IS YOUR CAREER GOING THE WAY YOU WANT?</h1>
      <p class="subhead">If not, do you feel stuck? Blocked? Frustrated? Don’t know what to do about this?</p>
      <h2 class="programme-title">RISING ABOVE HIDDEN CAREER DEAL BREAKERS</h2>
      <h3 class="format-label">FORMAT:</h3>
      <p class="format-text">4 MINI-WORKSHOPS + 2 SHORT ONLINE GROUP<br>COACHING SESSIONS BETWEEN WORKSHOPS</p>
      <div class="breakers">
        <h3 class="breakers__title">LEARN TO OVERCOME AND RISE ABOVE<br>THE 4 TOP HIDDEN CAREER DEAL BREAKERS FAST:</h3>
        <ol class="breakers__list">
          <li><span>1.</span><span>Microaggressions</span></li>
          <li><span>2.</span><span>Toxic black box team dynamics</span></li>
          <li><span>3.</span><span>Workplace snakes and other dysfunctional types</span></li>
          <li><span>4.</span><span>Disempowering Subconscious Algorithms no matter what – gedysfunctional subconscious roles</span></li>
        </ol>
      </div>
    </section>

    <div class="person person--left">
      <p class="person__name">DR. HELENA MARWICK</p>
      <p class="person__bio">Ph.D., PCC is a coach and somatic experience practitioner,<br>a team coach with diploma and a certified virtual team coach.</p>
    </div>

    <div class="contact">
      <p class="contact__title">FOR DATES, VENUE AND FURTHER INFORMATION<br>CONTACT HELENA OR CLARA AT:</p>
      <p class="contact__line">HELENA – helena@marwickcoaching.ch, Tel. 079 000 12 34</p>
      <p class="contact__line">CLARA – clara@lumenpath.ch, tel. 076 000 56 78</p>
    </div>

    <div class="person person--right">
      <p class="person__name">DR. CLARA VENNER</p>
      <p class="person__bio">PhD, CPC, is an American &amp; Swiss-Trained Work &amp; Organizational Psychologist, ICF-Certified Coach, Board Certified Hypnotherapist, Certified Naturopath (TEN) &amp; Certified Ayurvedic Practitioner.</p>
    </div>
  </main>
</body>
</html>
```